Coral Kyte
Business Card
Project: Coral Kyte
Coral Kyte - Software
Creative Brief
Professional
Tobias Hennard
EVP, Client & Partner Engagement
418 Pelling St 7th Floor San Francisco, CA 94187
tobias@coralkyte.us
www.coralkyte.us
Chat: tobias.hennard
Add the tagline to front of card: Solutions for a Mobile World
Add the tagline to back of card: Solutions for a Mobile World

```html
<!DOCTYPE html>
<html lang="en">
<head>
<meta charset="utf-8">
<title>Coral Kyte – Business Card</title>
<link rel="stylesheet" href="https://fonts.googleapis.com/css2?family=Nunito+Sans:wght@400;600;800&family=Open+Sans:wght@400;600&display=swap">
<style>
  :root {
    --blue: #2f5aa8;
    --blue-dark: #1f3f7e;
    --orange: #f08a24;
    --ink: #555a60;
    --card-top: #ffffff;
    --card-bottom: #e4e6e9;
    --stage: #dcdde0;
  }
  * { margin: 0; padding: 0; box-sizing: border-box; }
  html, body { width: 1200px; height: 901px; overflow: hidden; }
  body {
    background: var(--stage);
    font-family: "Open Sans", sans-serif;
    position: relative;
  }
  .card {
    position: absolute;
    width: 736px;
    height: 420px;
    left: 232px;
    border-radius: 26px;
    overflow: hidden;
    background: linear-gradient(180deg, var(--card-top) 0%, var(--card-bottom) 100%);
    box-shadow: 0 6px 18px rgba(0,0,0,0.18);
  }
  .card--back { top: 24px; }
  .card--front { top: 458px; }

  /* back */
  .back-mark {
    position: absolute;
    left: 50%; top: 70px;
    width: 170px; height: 170px;
    margin-left: -85px;
    border-radius: 50%;
    background: var(--blue);
  }
  .back-tagline {
    position: absolute;
    left: 0; right: 0; top: 290px;
    text-align: center;
    font-family: "Nunito Sans", sans-serif;
    font-weight: 600;
    font-size: 22px;
    color: var(--orange);
  }
  .back-web {
    position: absolute;
    left: 0; right: 0; top: 330px;
    text-align: center;
    font-size: 17px;
    letter-spacing: 2px;
    color: var(--blue);
  }

  /* front */
  .brand {
    position: absolute;
    left: 54px; top: 78px;
    display: flex; align-items: center; gap: 18px;
  }
  .brand-dot {
    width: 78px; height: 78px;
    border-radius: 50%;
    background: var(--blue);
    flex: none;
  }
  .brand-name {
    font-family: "Nunito Sans", sans-serif;
    font-weight: 800;
    font-size: 48px;
    line-height: 0.95;
    color: var(--blue-dark);
  }
  .brand-tagline {
    position: absolute;
    left: 150px; top: 192px;
    font-family: "Nunito Sans", sans-serif;
    font-weight: 600;
    font-size: 16px;
    letter-spacing: 0.5px;
    color: var(--orange);
  }
  .contact {
    position: absolute;
    left: 420px; top: 58px;
    color: var(--ink);
    font-size: 15px;
    line-height: 1.3;
  }
  .contact-name {
    font-size: 24px;
    font-weight: 600;
    color: var(--blue);
    line-height: 1.1;
  }
  .contact-title { font-size: 14px; margin-bottom: 14px; }
  .contact-address { margin-bottom: 16px; }
  .swoosh { position: absolute; left: 0; bottom: 0; width: 736px; height: 170px; }
  .web {
    position: absolute;
    left: 92px; bottom: 30px;
    font-size: 17px;
    letter-spacing: 3px;
    font-weight: 600;
    color: #fff;
  }
</style>
</head>
<body>

<section class="card card--back" aria-label="Card back">
  <div class="back-mark"></div>
  <p class="back-tagline">Solutions for a Mobile World</p>
  <p class="back-web">www.coralkyte.us</p>
</section>

<section class="card card--front" aria-label="Card front">
  <div class="brand">
    <div class="brand-dot"></div>
    <div class="brand-name">Coral<br>Kyte</div>
  </div>
  <p class="brand-tagline">Solutions for a Mobile World</p>

  <div class="contact">
    <p class="contact-name">Tobias Hennard</p>
    <p class="contact-title">EVP, Client &amp; Partner Engagement</p>
    <p class="contact-address">418 Pelling St<br>7th Floor<br>San Francisco, CA 94187</p>
    <p>415.555.0147<br>tobias@coralkyte.us<br>Chat: tobias.hennard</p>
  </div>

  <svg class="swoosh" viewBox="0 0 736 170" preserveAspectRatio="none" aria-hidden="true">
    <path d="M0 40 C 220 70, 520 60, 736 20 L736 170 L0 170 Z" fill="var(--orange)"/>
    <path d="M0 56 C 230 86, 520 80, 736 40 L736 170 L0 170 Z" fill="#ffffff"/>
    <path d="M0 64 C 240 96, 530 92, 736 52 L736 170 L0 170 Z" fill="var(--blue)"/>
  </svg>
  <p class="web">www.coralkyte.us</p>
</section>

</body>
</html>
```